Very new and innovative Web design for Property managers of Vacation rentals

We are looking for a new website design for travel agencies and property managers specialised on vacation rentals business, holiday villas and apartments.

The end users of this website are travellers who are looking for a vacation home for their next holiday: this is the reason why the website must be easy to use, attractive, professional, possibly elegant and focused on get new reservations.

This is a draft of our current website: https://demo5.holdiquay.com/
Please consider that we would like to have proposals with a totally different and innovative layout, surprise us!

These are the pages of the website:
• Homepage: feel free to redesign all the homepage as you wish, surprise us with something very new! Please consider that Property manager/Travel agencies usually want to have the opportunity to put in evidence groups of houses with specific characteristics (eg. villas with private swimming pool, apartment in big/small towns, villas with air co, etc…), destinations and tourist areas, and sometimes experiences or activities (please consider that the website layout must be suitable even if some of the previous sections are not used).
• Search page: we’d like to organise the results of the search page in three different ways:
o Grid
o Map
o List
• Property page: to illustrate the characteristics, descriptions, images, …. of the property. It is very important to put in evidence images of the property and to maintain the booking form (and the other call to action bottom – eg. whatsapp) always visible
• Custom pages: static pages composed usually by text, images and call to actions
• Contact us (general form)
• Info request (specific of a property form)
• Booking process
• Blog, organised in four pages:
o Home Page – introduction to the blog
o List of articles
o Single article
o Site Map (presentation of categories and sub-categories)

If possible, we’d prefer to receive the material in Adobe XD or similar so that we can obtain the three versions:
- smartphone
- tablet
- desktop

The website will be then developed in Bootstrap: as a result we’ll need the icons in SVG format (or the library used)

In attachment you can find the map of the website pages

```html
<!DOCTYPE html>
<html lang="en">
<head>
<meta charset="utf-8">
<title>Casavia – Exclusive Villas in Italy</title>
<link href="https://fonts.googleapis.com/css2?family=Bebas+Neue&family=Roboto:wght@400;500;700&display=swap" rel="stylesheet">
<style>
:root{
  --green:#1db47f;
  --green-dark:#159566;
  --ink:#1e1e1e;
  --text:#555;
  --muted:#8a8a8a;
  --light:#f6f6f6;
  --line:#e4e4e4;
  --footer:#1b1b1b;
}
*{box-sizing:border-box;margin:0;padding:0}
html,body{width:1200px;height:4673px;overflow:hidden}
body{font-family:'Roboto',Arial,sans-serif;color:var(--ink);background:#fff;position:relative}
.display{font-family:'Bebas Neue',Impact,sans-serif;font-weight:400;letter-spacing:.5px}
.green{color:var(--green)}
.eyebrow{font-family:'Roboto',sans-serif;font-weight:700;font-size:12px;letter-spacing:2.5px;text-align:center;color:var(--ink)}
.section-title{font-family:'Bebas Neue',Impact,sans-serif;font-size:50px;text-align:center;line-height:1;margin-top:8px}
.abs{position:absolute}
.btn{background:var(--green);color:#fff;font-weight:500;font-size:14px;text-transform:uppercase;display:flex;align-items:center;justify-content:center;gap:6px;border-radius:2px}

/* nav */
.nav{top:0;left:0;width:1200px;height:51px;background:#fff;display:flex;align-items:center}
.brand{display:flex;align-items:center;gap:8px;font-size:24px;color:var(--ink)}
.brand .dot{width:22px;height:22px;border-radius:50%;background:var(--green)}
.nav .brand{position:absolute;left:100px}
.nav-links{position:absolute;left:350px;display:flex;gap:38px;font-size:15px;font-weight:500;align-items:center}
.flags{position:absolute;left:906px;display:flex;gap:6px}
.signin{position:absolute;right:0;top:0;width:190px;height:51px;font-size:14px}

/* hero */
.hero{top:51px;left:0;width:1200px;height:596px;background:linear-gradient(90deg,#3f87c9 0%,#6fb0e0 35%,#b9c9cf 55%,#c8a46b 75%,#8e7b62 100%)}
.hero h1{position:absolute;left:97px;top:200px;font-size:64px;line-height:1.02;color:#fff}
.hero .btn{position:absolute;left:100px;top:352px;width:163px;height:41px}
.search{top:580px;left:242px;width:716px;height:131px;background:#fff;box-shadow:0 3px 14px rgba(0,0,0,.12);border-radius:4px}
.search h2{font-size:42px;text-align:center;margin-top:14px}
.search-row{position:absolute;left:15px;top:67px;display:flex;gap:10px;align-items:center}
.field{height:40px;border:1px solid var(--line);border-radius:2px;font-size:12px;color:var(--text);display:flex;align-items:center;justify-content:space-between;padding:0 12px}
.search .btn{width:129px;height:40px}

/* benefits */
.benefits{top:750px;left:0;width:1200px;height:592px;background:var(--light)}
.benefits p{width:1000px;margin:18px auto 0;font-size:13.5px;line-height:27px;text-align:center;color:var(--text)}
.tiles{position:absolute;left:100px;top:229px;display:flex;gap:15px}
.tile{width:242px}
.tile .ph{height:274px}
.tile span{display:block;text-align:center;font-size:15px;font-weight:700;margin-top:16px}

/* why */
.why{top:1342px;left:0;width:1200px;height:525px;background:#fff}
.why .lead{width:600px;margin:24px auto 0;text-align:center;font-size:13.5px;line-height:25px;color:var(--text)}
.features{position:absolute;left:100px;top:264px;display:flex;gap:40px}
.feature{width:307px;text-align:center}
.feature svg{display:block;margin:0 auto}
.feature h3{font-size:16px;font-weight:500;margin-top:16px;text-transform:uppercase}
.feature p{font-size:12px;line-height:25px;color:var(--text);margin-top:6px}

/* villas */
.villas{top:1867px;left:0;width:1200px;height:602px;background:var(--light)}
.cards{position:absolute;left:87px;top:187px;display:flex;gap:24px}
.card{width:238px;height:312px;background:transparent;padding:0;position:relative}
.card.active{background:#fff;box-shadow:0 2px 12px rgba(0,0,0,.12)}
.card .ph{height:152px;position:relative}
.card .specs{position:absolute;left:6px;right:6px;bottom:6px;height:28px;background:var(--green);color:#fff;font-size:9px;font-weight:700;display:flex;justify-content:space-around;align-items:center}
.card h3{font-size:21px;font-weight:500;margin:14px 0 0 2px}
.card p{font-size:11px;line-height:20px;color:var(--text);margin:6px 0 0 2px}
.card .foot{display:flex;justify-content:space-between;align-items:center;margin:12px 0 0 2px}
.price{color:var(--green);font-weight:700;font-size:13px}
.card .btn{width:70px;height:26px;font-size:12px}
.arrow{top:2200px}

/* amenities */
.amenities{top:2469px;left:0;width:1200px;height:749px;background:#fff}
.grid{position:absolute;left:105px;top:194px;display:grid;grid-template-columns:repeat(3,315px);column-gap:23px;row-gap:44px}
.amenity{height:201px;background:#fff;box-shadow:0 2px 12px rgba(0,0,0,.08);text-align:center;position:relative;padding-top:30px}
.amenity.active{background:var(--green);color:#fff}
.amenity h3{font-size:18px;font-weight:500;margin-top:10px}
.amenity p{font-size:12px;line-height:20px;color:var(--text);width:270px;margin:10px auto 0}
.amenity.active p{color:#fff}
.amenity .go{position:absolute;left:138px;bottom:-19px;width:38px;height:38px;border-radius:50%;background:var(--green);display:flex;align-items:center;justify-content:center;border:2px solid #fff}
.amenity svg.ic{stroke:var(--green)}
.amenity.active svg.ic{stroke:#fff}

/* app */
.app{top:3218px;left:0;width:1200px;height:393px;background:linear-gradient(90deg,#5f8ba7 0%,#7fa8c1 45%,#b9bab0 70%,#8c7b6b 100%)}
.phone{position:absolute;left:112px;top:64px;width:222px;height:329px;background:#f2f2f2;border-radius:30px 30px 0 0;padding:50px 12px 0}
.phone .screen{width:100%;height:100%;background:linear-gradient(180deg,#2c3a4a 0%,#55606e 35%,#fff 35%,#fff 100%)}
.app .eyebrow{position:absolute;left:388px;top:93px;color:#fff;text-align:left}
.app h2{position:absolute;left:388px;top:112px;color:#fff;font-size:38px;line-height:1.05}
.app .sub{position:absolute;left:388px;top:202px;color:#fff;font-size:14px}
.app .form{position:absolute;left:388px;top:236px;width:492px;height:46px;background:#fff;border-radius:2px;display:flex;align-items:center;justify-content:space-between;padding:0 4px 0 14px;font-size:14px;color:var(--text)}
.app .form .btn{width:128px;height:38px}

/* blog */
.blog{top:3611px;left:0;width:1200px;height:707px;background:var(--light)}
.posts{position:absolute;left:100px;top:196px;display:flex;gap:25px}
.post{width:317px;position:relative;height:420px}
.post .ph{height:236px}
.post .body{position:absolute;left:15px;top:196px;width:287px;height:212px;background:#fff;padding:18px 17px}
.date{font-size:12px;color:var(--text);display:flex;align-items:center;gap:8px}
.post h3{font-size:16px;font-weight:700;line-height:26px;margin-top:12px}
.post p{font-size:12px;line-height:21px;color:var(--muted);margin-top:6px}
.post a{display:inline-block;margin-top:8px;font-size:13px;font-weight:500;color:var(--green);text-decoration:underline}

/* footer */
.footer{top:4318px;left:0;width:1200px;height:355px;background:var(--footer);color:#fff}
.footer .brand{position:absolute;left:100px;top:90px;color:#fff;font-size:26px}
.socials{position:absolute;left:97px;top:158px;display:flex;gap:9px}
.socials i{width:36px;height:36px;border:1.5px solid #fff;border-radius:50%;display:block}
.fcol{position:absolute;top:88px;font-size:13px;line-height:28px}
.fcol h4{font-size:14px;font-weight:700;letter-spacing:.5px;line-height:20px;margin-bottom:10px}
.fcol .em{width:206px;height:36px;border:1px solid #666;font-size:12px;color:#ccc;display:flex;align-items:center;padding-left:10px}
.fcol .btn{width:206px;height:36px;margin-top:8px}
.copy{position:absolute;left:0;width:1200px;bottom:20px;text-align:center;font-size:12px;color:#ddd}
</style>
</head>
<body>

<header class="nav abs">
  <div class="brand"><span class="dot"></span>Casavia</div>
  <nav class="nav-links">
    <svg width="14" height="13" viewBox="0 0 14 13" fill="var(--green)"><path d="M7 0 14 6h-2v7H9V9H5v4H2V6H0z"/></svg>
    <span>Last Minute</span><span>Special Offers</span><span>Experience</span><span>Contact Us</span>
  </nav>
  <div class="flags">
    <svg width="34" height="20" viewBox="0 0 34 20"><rect width="34" height="20" fill="#24407a"/><path d="M0 0 34 20M34 0 0 20" stroke="#fff" stroke-width="4"/><rect x="14" width="6" height="20" fill="#fff"/><rect y="7" width="34" height="6" fill="#fff"/><rect x="15.5" width="3" height="20" fill="#c8102e"/><rect y="8.5" width="34" height="3" fill="#c8102e"/></svg>
    <svg width="34" height="20" viewBox="0 0 33 20"><rect width="11" height="20" fill="#1a9b47"/><rect x="11" width="11" height="20" fill="#fff"/><rect x="22" width="11" height="20" fill="#d22630"/></svg>
  </div>
  <div class="btn signin"><svg width="12" height="12" viewBox="0 0 12 12" fill="none" stroke="#fff" stroke-width="1.5"><path d="M5 2H1v8h4M4 6h7M8 3l3 3-3 3"/></svg>Sign-in or join</div>
</header>

<section class="hero abs" role="img" aria-label="Smiling traveller with sunglasses and backpack in front of a sunlit gothic tower under a stone arch">
  <h1 class="display">Exclusive villas<br>in Italy</h1>
  <div class="btn">Get started</div>
</section>

<div class="search abs">
  <h2 class="display">Search villas</h2>
  <div class="search-row">
    <div class="field" style="width:135px">Destination <svg width="9" height="12" viewBox="0 0 9 12"><path d="M4.5 0A4.5 4.5 0 0 0 0 4.5C0 8 4.5 12 4.5 12S9 8 9 4.5A4.5 4.5 0 0 0 4.5 0zm0 6.3a1.8 1.8 0 1 1 0-3.6 1.8 1.8 0 0 1 0 3.6z" fill="#333"/></svg></div>
    <div class="field" style="width:110px">Check In <svg width="12" height="11" viewBox="0 0 12 11" fill="none" stroke="#777"><rect x=".5" y="1.5" width="11" height="9"/><path d="M.5 4h11"/></svg></div>
    <div class="field" style="width:110px">Check Out <svg width="12" height="11" viewBox="0 0 12 11" fill="none" stroke="#777"><rect x=".5" y="1.5" width="11" height="9"/><path d="M.5 4h11"/></svg></div>
    <div class="field" style="width:126px">Travelers <svg width="16" height="12" viewBox="0 0 16 12" fill="#333"><circle cx="5" cy="3" r="3"/><path d="M0 12c0-4 10-4 10 0zM12 6h4l-2 2z"/></svg></div>
    <div class="btn"><svg width="13" height="13" viewBox="0 0 13 13" fill="none" stroke="#fff" stroke-width="2"><circle cx="5.5" cy="5.5" r="4"/><path d="M8.5 8.5 12 12"/></svg>Search</div>
  </div>
</div>

<section class="benefits abs">
  <div class="eyebrow" style="margin-top:17px">OUR BENEFITS</div>
  <h2 class="section-title">Looking for an <span class="green">exclusive holiday?</span></h2>
  <p>Browse our vacation rental selections If you are looking for a real experiences, our portal is the right solution. Our vacation homes are all located in Italy and we take care of them and their owners at every time. Our goal is give to our guest authentic taste of holiday and our country. Our team is always ready to assure the best time and take care of you! Add a local experience to your stay with us: by diving into our local "network" you can have the unique chance to discover and travel our culture through the eye of a local...!</p>
  <div class="tiles">
    <div class="tile"><div class="ph" role="img" aria-label="Modern luxury villa lit at dusk" style="background:linear-gradient(180deg,#6a5246,#3a2a24 60%,#c98b5a)"></div><span>Luxury Villas</span></div>
    <div class="tile"><div class="ph" role="img" aria-label="Table with plates of local food and vegetables" style="background:linear-gradient(160deg,#c9c3bb,#6b5847 50%,#4d6a3a)"></div><span>Experiences</span></div>
    <div class="tile"><div class="ph" role="img" aria-label="Couple reading a map in front of a cathedral" style="background:linear-gradient(180deg,#d8d0bf,#a89577 55%,#5f5446)"></div><span>Browes All Vacation Rentals</span></div>
    <div class="tile"><div class="ph" role="img" aria-label="Sun hat floating in a blue swimming pool" style="background:linear-gradient(180deg,#3f8fcf,#6fb5e6 70%,#e9eef2)"></div><span>Last Minute Deals</span></div>
  </div>
</section>

<section class="why abs">
  <div class="eyebrow" style="margin-top:93px">WHY RENT WITH US</div>
  <h2 class="section-title">Why choose <span class="green">Casavia</span></h2>
  <p class="lead">Lorem ipsum dolor sit amet, consectetur adipiscing elit, sed do eiusmod tempor incididunt ut labore et dolore magna aliqua. Ut enim ad minim veniam, quis no</p>
  <div class="features">
    <div class="feature">
      <svg width="70" height="52" viewBox="0 0 70 52" fill="none" stroke="var(--green)" stroke-width="1.6"><circle cx="33" cy="22" r="13"/><path d="M42 31 54 45"/><path d="M27 24l6-6 6 6v6H27z"/><circle cx="10" cy="20" r="1.5"/><circle cx="62" cy="12" r="1.5"/></svg>
      <h3>Best Results</h3>
      <p>Sed ut peratis unde omnis iste natus error sit voluptatem accusantium doloremque launtium, totam rem aperiam, eaque ipsa quae ab illo inv</p>
    </div>
    <div class="feature">
      <svg width="70" height="56" viewBox="0 0 70 56" fill="none" stroke="var(--green)" stroke-width="1.6"><path d="M22 18 34 8l12 10v12H22z"/><rect x="30" y="20" width="8" height="10"/><circle cx="38" cy="44" r="8"/><path d="M38 40v8M14 34h10l6 6"/><circle cx="8" cy="30" r="1.5"/><circle cx="62" cy="22" r="1.5"/></svg>
      <h3>Best Value</h3>
      <p>Sed ut peratis unde omnis iste natus error sit voluptatem accusantium doloremque launtium, totam rem aperiam, eaque ipsa quae ab illo inv</p>
    </div>
    <div class="feature">
      <svg width="70" height="52" viewBox="0 0 70 52" fill="none" stroke="var(--green)" stroke-width="1.6"><path d="M10 22l10-8 8 4 8-4 10 2 10 6-8 14-10 8-8-4-10-6z"/><path d="M28 18l10 8M30 30l6 6M24 34l6 4"/><circle cx="8" cy="40" r="1.5"/><circle cx="62" cy="14" r="1.5"/></svg>
      <h3>Best Service</h3>
      <p>Sed ut peratis unde omnis iste natus error sit voluptatem accusantium doloremque launtium, totam rem aperiam, eaque ipsa quae ab illo inv</p>
    </div>
  </div>
</section>

<section class="villas abs">
  <div class="eyebrow" style="margin-top:94px">QUICK SEARCH</div>
  <h2 class="section-title">New villas &amp; <span class="green">vacation rentals</span></h2>
  <div class="cards">
    <div class="card">
      <div class="ph" role="img" aria-label="Modern white villa with swimming pool" style="background:linear-gradient(180deg,#8fc0e6,#e8e6e0 50%,#3aa8d8)"><div class="specs"><span>7 BED</span><span>7 BATH</span><span>2K SQFT</span></div></div>
      <h3>Agriturismo Il Poggio</h3>
      <p>il casale è immerson nella campagna toscana ma a soli 3 km dal paese più vicino dove</p>
      <div class="foot"><span class="price">$###,###</span><span class="btn">View</span></div>
    </div>
    <div class="card active">
      <div class="ph" role="img" aria-label="Stone villa with pool and garden" style="background:linear-gradient(180deg,#6aaede,#d9d2c2 55%,#4ab3dd)"><div class="specs"><span>7 BED</span><span>7 BATH</span><span>2K SQFT</span></div></div>
      <h3 style="margin-left:8px">Villa 2</h3>
      <p style="margin-left:8px">il casale è immerson nella campagna toscana ma a soli 3 km dal paese più vicino dove</p>
      <div class="foot" style="margin:12px 8px 0"><span class="price">$###,###</span><span class="btn">View</span></div>
    </div>
    <div class="card">
      <div class="ph" role="img" aria-label="Villa garden with large pool and slide" style="background:linear-gradient(180deg,#3b7fc8,#6f8e4e 45%,#3cb0e0)"><div class="specs"><span>7 BED</span><span>7 BATH</span><span>2K SQFT</span></div></div>
      <h3>Villa 3</h3>
      <p>il casale è immerson nella campagna toscana ma a soli 3 km dal paese più vicino dove</p>
      <div class="foot"><span class="price">$###,###</span><span class="btn">View</span></div>
    </div>
    <div class="card">
      <div class="ph" role="img" aria-label="Farmhouse pool surrounded by olive trees" style="background:linear-gradient(180deg,#b9d6e6,#6d8a4c 50%,#49b6dd)"><div class="specs"><span>7 BED</span><span>7 BATH</span><span>2K SQFT</span></div></div>
      <h3>Farmhouse In Tuscany</h3>
      <p>il casale è immerson nella campagna toscana ma a soli 3 km dal paese più vicino dove</p>
      <div class="foot"><span class="price">$###,###</span><span class="btn">View</span></div>
    </div>
  </div>
</section>
<svg class="abs arrow" style="left:48px" width="16" height="30" viewBox="0 0 16 30" fill="none" stroke="#333" stroke-width="2"><path d="M14 2 2 15l12 13"/></svg>
<svg class="abs arrow" style="left:1134px" width="16" height="30" viewBox="0 0 16 30" fill="none" stroke="#333" stroke-width="2"><path d="M2 2l12 13L2 28"/></svg>

<section class="amenities abs">
  <div class="eyebrow" style="margin-top:100px">OUR FACILITIES</div>
  <h2 class="section-title">Amenities &amp; <span class="green">facilities</span></h2>
  <div class="grid">
    <div class="amenity"><svg class="ic" width="44" height="34" viewBox="0 0 44 34" fill="none" stroke-width="1.6"><path d="M12 28V4a4 4 0 0 1 8 0M26 28V4a4 4 0 0 1 8 0M12 12h14M12 20h14M2 30c4-3 6 3 10 0s6 3 10 0 6 3 10 0 6 3 10 0"/></svg><h3>PRIVATE SWIMMING POOL</h3><p>Sed ut perspiciatis unde omnis iste natus error sit voluptatecusanum doloremque laudantium, totam rem aperiam, eaque ipsa</p><span class="go"><svg width="14" height="12" viewBox="0 0 14 12" fill="none" stroke="#fff" stroke-width="1.6"><path d="M1 6h12M8 1l5 5-5 5"/></svg></span></div>
    <div class="amenity active"><svg class="ic" width="60" height="34" viewBox="0 0 60 34" fill="none" stroke-width="1.6"><circle cx="12" cy="22" r="10"/><circle cx="48" cy="22" r="10"/><path d="M12 22l10-14h16l10 14M22 8l8 14 8-14M18 4h8M36 4h6"/></svg><h3>BICYLES</h3><p>Sed ut perspiciatis unde omnis iste natus error sit voluptatecusanum doloremque laudantium, totam rem aperiam, eaque ipsa</p><span class="go"><svg width="14" height="12" viewBox="0 0 14 12" fill="none" stroke="#fff" stroke-width="1.6"><path d="M1 6h12M8 1l5 5-5 5"/></svg></span></div>
    <div class="amenity"><svg class="ic" width="66" height="30" viewBox="0 0 66 30" fill="none" stroke-width="1.6"><path d="M3 22v-6l8-2 8-8h24l10 8 10 2v6H3z"/><circle cx="16" cy="22" r="5"/><circle cx="50" cy="22" r="5"/><path d="M22 14h28"/></svg><h3>TRANSFER</h3><p>Sed ut perspiciatis unde omnis iste natus error sit voluptatecusanum doloremque laudantium, totam rem aperiam, eaque ipsa</p><span class="go"><svg width="14" height="12" viewBox="0 0 14 12" fill="none" stroke="#fff" stroke-width="1.6"><path d="M1 6h12M8 1l5 5-5 5"/></svg></span></div>
    <div class="amenity"><svg class="ic" width="44" height="36" viewBox="0 0 44 36" fill="none" stroke-width="1.6"><rect x="4" y="16" width="36" height="18"/><path d="M22 16v18M10 4v10M16 2v12M30 6h6v10M8 22h8M28 22h8"/></svg><h3>KITCHEN</h3><p>Sed ut perspiciatis unde omnis iste natus error sit voluptatecusanum doloremque laudantium, totam rem aperiam, eaque ipsa</p><span class="go"><svg width="14" height="12" viewBox="0 0 14 12" fill="none" stroke="#fff" stroke-width="1.6"><path d="M1 6h12M8 1l5 5-5 5"/></svg></span></div>
    <div class="amenity"><svg class="ic" width="44" height="34" viewBox="0 0 44 34" fill="none" stroke-width="1.6"><rect x="4" y="4" width="36" height="22"/><path d="M16 32h12M22 26v6"/></svg><h3>SATELLITE TV</h3><p>Sed ut perspiciatis unde omnis iste natus error sit voluptatecusanum doloremque laudantium, totam rem aperiam, eaque ipsa</p><span class="go"><svg width="14" height="12" viewBox="0 0 14 12" fill="none" stroke="#fff" stroke-width="1.6"><path d="M1 6h12M8 1l5 5-5 5"/></svg></span></div>
    <div class="amenity"><svg class="ic" width="44" height="36" viewBox="0 0 44 36" fill="none" stroke-width="1.6"><path d="M16 4h16v28H16zM16 12h16"/><circle cx="24" cy="22" r="4"/><path d="M6 10v20M4 10h4M38 8v8M36 20h4"/></svg><h3>BATHROOM AMENITIES</h3><p>Sed ut perspiciatis unde omnis iste natus error sit voluptatecusanum doloremque laudantium, totam rem aperiam, eaque ipsa</p><span class="go"><svg width="14" height="12" viewBox="0 0 14 12" fill="none" stroke="#fff" stroke-width="1.6"><path d="M1 6h12M8 1l5 5-5 5"/></svg></span></div>
  </div>
</section>

<section class="app abs" role="img" aria-label="Smiling man looking at his smartphone">
  <div class="phone"><div class="screen" role="img" aria-label="App screen showing a property listing with price and details"></div></div>
  <div class="eyebrow">GET THE APP</div>
  <h2 class="display">Search for new villas &amp; vacation<br>rentals on your phone</h2>
  <div class="sub">Enter your phone number to get App's link instantly and download now</div>
  <div class="form">Phone Number<span class="btn">Get app link</span></div>
</section>

<section class="blog abs">
  <div class="eyebrow" style="margin-top:92px">LATEST UPDATES</div>
  <h2 class="section-title">Latest blog <span class="green">post</span></h2>
  <div class="posts">
    <div class="post"><div class="ph" role="img" aria-label="Traveller with suitcase entering a sunlit hotel room" style="background:linear-gradient(135deg,#3d3128,#c79b5f 55%,#f1d9a6)"></div>
      <div class="body"><div class="date"><svg width="20" height="18" viewBox="0 0 20 18" fill="none" stroke="var(--green)"><rect x=".5" y="2.5" width="19" height="15"/><path d="M.5 6h19M5 0v4M15 0v4"/></svg>November 14, 2021</div><h3>Lorem ipsum doloet, consectetur adipiscing</h3><p>Lorem ipsum dolor sit amet, consectetur adipiscing elit, sed do eiusmod tempor incididunt ut labore et dolore</p><a>READ MORE</a></div></div>
    <div class="post"><div class="ph" role="img" aria-label="Traveller wearing a mask sitting with luggage in an airport" style="background:linear-gradient(180deg,#8a9fb8,#3a5b8e 50%,#c39b2c)"></div>
      <div class="body"><div class="date"><svg width="20" height="18" viewBox="0 0 20 18" fill="none" stroke="var(--green)"><rect x=".5" y="2.5" width="19" height="15"/><path d="M.5 6h19M5 0v4M15 0v4"/></svg>November 14, 2021</div><h3>Lorem ipsum doloet, consectetur adipiscing</h3><p>Lorem ipsum dolor sit amet, consectetur adipiscing elit, sed do eiusmod tempor incididunt ut labore et dolore</p><a>READ MORE</a></div></div>
    <div class="post"><div class="ph" role="img" aria-label="World map with camera, passport and phone on a desk" style="background:linear-gradient(135deg,#d7c69d,#8fb0a8 50%,#3f4a4e)"></div>
      <div class="body"><div class="date"><svg width="20" height="18" viewBox="0 0 20 18" fill="none" stroke="var(--green)"><rect x=".5" y="2.5" width="19" height="15"/><path d="M.5 6h19M5 0v4M15 0v4"/></svg>November 14, 2021</div><h3>Lorem ipsum doloet, consectetur adipiscing</h3><p>Lorem ipsum dolor sit amet, consectetur adipiscing elit, sed do eiusmod tempor incididunt ut labore et dolore</p><a>READ MORE</a></div></div>
  </div>
</section>

<footer class="footer abs">
  <div class="brand"><span class="dot"></span>Casavia</div>
  <div class="socials"><i></i><i></i><i></i><i></i></div>
  <div class="fcol" style="left:322px"><h4>CONTACT US</h4>
    <div>&#9679; via dei Cipressi 42</div><div style="font-weight:500">50120 Collebruna, Siena (Italy)</div><div>&#9742; +39 055 0142876</div><div>&#9993; info@casavia.com</div></div>
  <div class="fcol" style="left:593px"><h4>QUICK LINKS</h4>
    <div>Home</div><div>Last Minute</div><div>Special Offers</div><div>Experience</div><div>Contact Us</div></div>
  <div class="fcol" style="left:752px"><h4>OUR VILLAS</h4>
    <div>Villa 6.1</div><div>Villa 6.2</div><div>Villa 6.3</div><div>Villa 6.4</div><div>Villa 6.5</div><div>Villa 6.6</div></div>
  <div class="fcol" style="left:892px"><h4>FEEL GOOD EMAILS.<br>INQUIRE BELOW.</h4>
    <div class="em">Email</div><div class="btn">Submit</div></div>
  <div class="copy">© 2021CASAVIA. All Rights Reserved.</div>
</footer>

</body>
</html>
```